Bramblewick Painting Epoxy Flyer

We need a promotional flyer for a new epoxy floor coatings division of our painting company. We do epoxy garage floor coatings and paver sealing. It needs to be based on and very similar to the attached flyer. The garage floor picture needs to look more realistic, and the before and after pavers pictures should look less shiny but still a good contrast. Include attached logo

```html
<!DOCTYPE html>
<html lang="en">
<head>
<meta charset="utf-8">
<title>Bramblewick Painting Epoxy Flyer</title>
<link href="https://fonts.googleapis.com/css2?family=Oswald:wght@300;400;500;600&family=Montserrat:wght@700;800&family=PT+Serif:ital,wght@1,700&family=Roboto:wght@900&display=swap" rel="stylesheet">
<style>
  :root {
    --blue: #0a3f99;
    --navy: #06287a;
    --green: #3f8f12;
    --ink: #141414;
    --paper: #fbfbfb;
    --blue-tint: #e8effb;
    --green-tint: #eef8e6;
    --line-green: #5aa02c;
  }
  * { box-sizing: border-box; margin: 0; padding: 0; }
  html, body { width: 880px; height: 1200px; overflow: hidden; background: var(--paper); }
  .flyer { position: relative; width: 880px; height: 1200px; background: var(--paper); font-family: "Oswald", sans-serif; color: var(--ink); }

  .brand { position: absolute; top: 58px; left: 0; width: 880px; display: flex; justify-content: center; align-items: center; gap: 14px; }
  .brand-dot { width: 44px; height: 44px; border-radius: 50%; background: var(--green); }
  .brand-name { font-family: "Montserrat", sans-serif; font-weight: 700; font-size: 30px; letter-spacing: 1px; color: #3a3a3a; }

  .section-label { position: absolute; top: 178px; left: 50px; width: 780px; display: flex; align-items: flex-end; gap: 4px; }
  .section-label span { font-family: "Montserrat", sans-serif; font-weight: 800; font-size: 21px; line-height: 1; }
  .section-label i { flex: 1; height: 1.5px; background: var(--line-green); margin-bottom: 3px; }

  .photo { position: absolute; }
  .photo-garage-before { left: 50px; top: 210px; width: 244px; height: 310px; background: linear-gradient(180deg, #d6d0c4 0 17%, #8f8676 17%, #9c9383 45%, #857c6c 100%); }
  .photo-garage-after { left: 300px; top: 210px; width: 264px; height: 310px; background: linear-gradient(180deg, #d9d3c6 0 17%, #8e9094 17%, #7a7c80 60%, #6c6e72 100%); }
  .photo-paver-before { left: 570px; top: 210px; width: 262px; height: 152px; background: linear-gradient(180deg, #7d6e5e 0 15%, #6e6558 15%, #7d7366 100%); }
  .photo-paver-after { left: 570px; top: 368px; width: 262px; height: 152px; background: linear-gradient(180deg, #7d6e5e 0 15%, #8a5e3c 15%, #9a6b45 100%); }

  .tag { position: absolute; font-family: "Montserrat", sans-serif; font-weight: 800; font-size: 19px; color: #fff; padding: 4px 12px; line-height: 1.2; }
  .tag-before { background: var(--blue); }
  .tag-after { background: var(--green); }

  .headline { position: absolute; top: 532px; left: 0; width: 880px; text-align: center; font-weight: 500; font-size: 46px; letter-spacing: -0.3px; line-height: 1.1; }
  .headline .blue { color: var(--blue); }
  .headline .green { color: var(--green); }
  .subline { position: absolute; top: 600px; left: 0; width: 880px; display: flex; justify-content: center; align-items: center; gap: 10px; font-family: "PT Serif", serif; font-style: italic; font-weight: 700; font-size: 21px; }
  .subline i { width: 40px; height: 2px; background: var(--blue); }

  .service { position: absolute; top: 644px; width: 366px; height: 168px; border-radius: 6px; }
  .service-epoxy { left: 68px; background: var(--blue-tint); }
  .service-paver { left: 450px; background: var(--green-tint); }
  .service h2 { font-weight: 500; font-size: 22px; color: #fff; text-align: center; height: 37px; line-height: 37px; border-radius: 6px 6px 0 0; }
  .service-epoxy h2 { background: var(--blue); }
  .service-paver h2 { background: var(--green); }
  .service ul { list-style: none; padding: 12px 0 0 54px; }
  .service li { display: flex; align-items: center; gap: 6px; font-weight: 300; font-size: 16.5px; line-height: 25px; color: #1c1c1c; }
  .service li svg { flex: none; }

  .trust { position: absolute; top: 828px; left: 68px; width: 748px; height: 232px; background: var(--blue); border-radius: 6px; overflow: hidden; }
  .trust h3 { height: 48px; line-height: 48px; background: var(--navy); color: #fff; text-align: center; font-weight: 500; font-size: 24px; }
  .trust-row { display: flex; height: 184px; }
  .trust-item { flex: 1; display: flex; flex-direction: column; align-items: center; padding-top: 24px; color: #fff; font-weight: 400; font-size: 17px; line-height: 1.2; text-align: center; }
  .trust-item + .trust-item { background: linear-gradient(90deg, rgba(0,0,0,.12), transparent 30px); }
  .badge { width: 84px; height: 84px; border-radius: 50%; border: 3px solid var(--green); padding: 5px; margin-bottom: 14px; }
  .badge div { width: 100%; height: 100%; border-radius: 50%; background: #fff; display: flex; align-items: center; justify-content: center; }

  .cta-title { position: absolute; top: 1070px; left: 0; width: 880px; display: flex; justify-content: center; align-items: center; gap: 12px; color: var(--blue); font-weight: 500; font-size: 29px; }
  .cta-title i { width: 26px; height: 2.5px; background: var(--blue); }
  .phone { position: absolute; top: 1110px; left: 0; width: 880px; display: flex; justify-content: center; align-items: center; gap: 10px; font-family: "Roboto", sans-serif; font-weight: 900; font-size: 52px; letter-spacing: 0.5px; line-height: 1; }
  .promise { position: absolute; top: 1160px; left: 0; width: 880px; text-align: center; color: var(--green); font-weight: 300; font-style: italic; font-size: 17px; }

  .foot-bar { position: absolute; bottom: 0; height: 8px; }
  .foot-left { left: 0; width: 228px; background: var(--blue); }
  .foot-mid { left: 238px; width: 404px; background: var(--green); }
  .foot-right { left: 652px; width: 228px; background: var(--blue); }
</style>
</head>
<body>
<main class="flyer">
  <header class="brand">
    <span class="brand-dot"></span>
    <span class="brand-name">BRAMBLEWICK PAINTING</span>
  </header>

  <div class="section-label"><span>EPROXY</span><i></i></div>

  <div class="photo photo-garage-before" role="img" aria-label="Stained, worn concrete garage floor before coating"></div>
  <div class="photo photo-garage-after" role="img" aria-label="Grey flake epoxy garage floor after coating"></div>
  <div class="photo photo-paver-before" role="img" aria-label="Faded grey paver patio before sealing"></div>
  <div class="photo photo-paver-after" role="img" aria-label="Restored warm brown paver patio after sealing"></div>

  <span class="tag tag-before" style="left:194px; top:424px;">BEFORE</span>
  <span class="tag tag-after" style="left:300px; top:424px;">AFTER</span>
  <span class="tag tag-before" style="left:682px; top:332px;">BEFORE</span>
  <span class="tag tag-after" style="left:682px; top:372px;">AFTER</span>

  <h1 class="headline">Upgarde Your <span class="blue">Garage</span> <span class="blue">&amp;</span> <span class="green">Driveway</span></h1>
  <p class="subline"><i></i>From worn-out to like new<i></i></p>

  <section class="service service-epoxy">
    <h2>EPROXY FLOOR COATINGS</h2>
    <ul>
      <li><svg width="18" height="18" viewBox="0 0 20 20"><circle cx="10" cy="10" r="8" fill="none" stroke="#0a3f99" stroke-width="2"/><path d="M6 10l3 3 8-9" fill="none" stroke="#0a3f99" stroke-width="2.2"/></svg>Durable, long-lasting finish</li>
      <li><svg width="18" height="18" viewBox="0 0 20 20"><circle cx="10" cy="10" r="8" fill="none" stroke="#0a3f99" stroke-width="2"/><path d="M6 10l3 3 8-9" fill="none" stroke="#0a3f99" stroke-width="2.2"/></svg>Slip-resistant texture</li>
      <li><svg width="18" height="18" viewBox="0 0 20 20"><circle cx="10" cy="10" r="8" fill="none" stroke="#0a3f99" stroke-width="2"/><path d="M6 10l3 3 8-9" fill="none" stroke="#0a3f99" stroke-width="2.2"/></svg>Covers cracks &amp; imperfections</li>
      <li><svg width="18" height="18" viewBox="0 0 20 20"><circle cx="10" cy="10" r="8" fill="none" stroke="#0a3f99" stroke-width="2"/><path d="M6 10l3 3 8-9" fill="none" stroke="#0a3f99" stroke-width="2.2"/></svg>Easy to clean &amp; maintain</li>
    </ul>
  </section>

  <section class="service service-paver">
    <h2>PAVER SEALING</h2>
    <ul>
      <li><svg width="18" height="18" viewBox="0 0 20 20"><circle cx="10" cy="10" r="8" fill="none" stroke="#3f8f12" stroke-width="2"/><path d="M6 10l3 3 8-9" fill="none" stroke="#3f8f12" stroke-width="2.2"/></svg>Restores color &amp; enhances appearance</li>
      <li><svg width="18" height="18" viewBox="0 0 20 20"><circle cx="10" cy="10" r="8" fill="none" stroke="#3f8f12" stroke-width="2"/><path d="M6 10l3 3 8-9" fill="none" stroke="#3f8f12" stroke-width="2.2"/></svg>Protects from sun fading</li>
      <li><svg width="18" height="18" viewBox="0 0 20 20"><circle cx="10" cy="10" r="8" fill="none" stroke="#3f8f12" stroke-width="2"/><path d="M6 10l3 3 8-9" fill="none" stroke="#3f8f12" stroke-width="2.2"/></svg>Helps prevent weeds &amp; sand loss</li>
      <li><svg width="18" height="18" viewBox="0 0 20 20"><circle cx="10" cy="10" r="8" fill="none" stroke="#3f8f12" stroke-width="2"/><path d="M6 10l3 3 8-9" fill="none" stroke="#3f8f12" stroke-width="2.2"/></svg>Easier to clean &amp; maintain</li>
    </ul>
  </section>

  <section class="trust">
    <h3>Practical upgardes that protect and improve your home</h3>
    <div class="trust-row">
      <div class="trust-item">
        <div class="badge"><div>
          <svg width="44" height="44" viewBox="0 0 44 44"><path d="M22 5l14 5v10c0 9-6 16-14 19C14 36 8 29 8 20V10z" fill="none" stroke="#0a3f99" stroke-width="2.5"/><path d="M15 21l5 5 10-11" fill="none" stroke="#3f8f12" stroke-width="3"/></svg>
        </div></div>
        Licensed &amp; Insured
      </div>
      <div class="trust-item">
        <div class="badge"><div>
          <svg width="44" height="44" viewBox="0 0 44 44"><path d="M10 34l16-16" stroke="#0a3f99" stroke-width="4" stroke-linecap="round"/><circle cx="30" cy="14" r="6" fill="none" stroke="#0a3f99" stroke-width="2.5"/><path d="M12 10l22 22" stroke="#3f8f12" stroke-width="4" stroke-linecap="round"/><circle cx="11" cy="34" r="3" fill="#fff" stroke="#0a3f99" stroke-width="2"/></svg>
        </div></div>
        Family-Owned Local<br>Business
      </div>
      <div class="trust-item">
        <div class="badge"><div>
          <svg width="44" height="44" viewBox="0 0 44 44"><path d="M22 30c-6-7-9-11-9-15a9 9 0 0118 0c0 4-3 8-9 15z" fill="none" stroke="#3f8f12" stroke-width="2.5"/><circle cx="22" cy="15" r="3.5" fill="none" stroke="#3f8f12" stroke-width="2"/><path d="M8 38l5-8h18l5 8z" fill="none" stroke="#0a3f99" stroke-width="2.2"/></svg>
        </div></div>
        Serving Prescott &amp;<br>Surrounding Areas
      </div>
    </div>
  </section>

  <p class="cta-title"><i></i>CALL FOR A FREE EXTIMATE<i></i></p>
  <p class="phone">
    <svg width="44" height="44" viewBox="0 0 44 44"><path d="M12 6l6 8-4 4c2 5 6 9 11 11l4-4 8 6-3 6c-14 1-29-14-28-28z" fill="none" stroke="#3f8f12" stroke-width="2.5" stroke-linejoin="round"/><path d="M27 8a10 10 0 019 9M26 13a5 5 0 015 5" fill="none" stroke="#3f8f12" stroke-width="2.2"/></svg>
    928-555-0174
  </p>
  <p class="promise">Fast, professional service you can trust</p>

  <span class="foot-bar foot-left"></span>
  <span class="foot-bar foot-mid"></span>
  <span class="foot-bar foot-right"></span>
</main>
</body>
</html>
```